Banner for back of trucks

We make a product that is called "Brindo".
It attaches to the side of hay balers and automatically applies tags to bales as they are being made.
We require a simple / modern banner design that will be affixed to the back of hay trucks showing that the hay on board has been Marked by Brindo.
The banner will be 52x91cm (landscape)
The banner needs to say "Marked by Brindo" using the company logo.
It also needs the website "www.brindo.com.au" displayed.
We have attached an image of our logo, the product itself and the back of a truck it will be attached to for reference.

```html
<!DOCTYPE html>
<html lang="en">
<head>
<meta charset="utf-8">
<title>Marked by Brindo – Truck Banner</title>
<link rel="stylesheet" href="https://fonts.googleapis.com/css2?family=Montserrat:wght@600;700;800&display=swap">
<style>
  :root {
    --stage: #383838;
    --stage-light: #424242;
    --hay-dark: #a9a68e;
    --hay-mid: #b7b39c;
    --hay-light: #c9c6b0;
    --orange: #f9ac41;
    --ink: #2e251b;
    --brown: #5a4a3e;
    --white: #ffffff;
    --green-dark: #2f6a2a;
    --green: #3f8a36;
    --steel: #e4e4de;
  }
  html, body {
    margin: 0;
    width: 1200px;
    height: 1200px;
    overflow: hidden;
  }
  body {
    background: radial-gradient(ellipse at 50% 40%, var(--stage-light), var(--stage) 70%);
    font-family: "Montserrat", sans-serif;
    position: relative;
  }
  .banner {
    position: absolute;
    left: 73px;
    top: 299px;
    width: 1053px;
    height: 602px;
    overflow: hidden;
  }
  .banner__backdrop {
    position: absolute;
    inset: 0;
    background:
      linear-gradient(90deg, var(--hay-dark) 0%, var(--hay-mid) 60%, var(--hay-light) 100%);
  }
  .product-photo {
    position: absolute;
    left: 45px;
    top: 44px;
    width: 304px;
    height: 304px;
    border-radius: 50%;
    border: 7px solid var(--white);
    box-sizing: border-box;
    background:
      radial-gradient(circle at 45% 50%, var(--steel) 0 22%, transparent 23%),
      linear-gradient(160deg, var(--green) 0%, var(--green-dark) 100%);
  }
  .tagline {
    position: absolute;
    left: 528px;
    top: 34px;
    width: 378px;
    height: 66px;
    background: var(--orange);
    border-radius: 6px;
    color: var(--ink);
    font-weight: 800;
    font-size: 50px;
    line-height: 66px;
    text-align: center;
    letter-spacing: 1px;
  }
  .brand-name {
    position: absolute;
    left: 410px;
    top: 120px;
    width: 630px;
    text-align: center;
    color: var(--brown);
    font-weight: 600;
    font-size: 158px;
    line-height: 200px;
  }
  .phone-band {
    position: absolute;
    left: 0;
    top: 377px;
    width: 1000px;
    height: 117px;
    background: linear-gradient(90deg, rgba(249,172,65,0) 0%, var(--orange) 12%, var(--orange) 88%, rgba(249,172,65,0) 100%);
  }
  .phone-number {
    position: absolute;
    left: 0;
    top: 377px;
    width: 1000px;
    height: 117px;
    margin: 0;
    text-align: center;
    color: var(--ink);
    font-weight: 800;
    font-size: 118px;
    line-height: 117px;
    letter-spacing: -1px;
  }
  .website {
    position: absolute;
    left: 0;
    top: 510px;
    width: 1000px;
    text-align: center;
    color: #111;
    font-weight: 800;
    font-size: 57px;
    line-height: 70px;
    letter-spacing: 3px;
  }
</style>
</head>
<body>
  <section class="banner">
    <div class="banner__backdrop" role="img" aria-label="Faded photo of stacked hay bales in a field"></div>
    <div class="product-photo" role="img" aria-label="Photo of the Brindo tagging unit mounted on a green hay baler"></div>
    <div class="tagline">MARKED BY</div>
    <div class="brand-name">Brindo</div>
    <div class="phone-band"></div>
    <p class="phone-number">04 5550 1847</p>
    <div class="website">WWW.BRINDO.COM.AU</div>
  </section>
</body>
</html>
```